Mabel's Fitness Business Cards

I would like my business cards to look expensive and sophisticated using my logo and the information below.

FRONT
Mabel’s Fitness logo

Tag line Become your happiest, healthiest and strongest self

Mabel Quint Harlow
Personal Trainer

e. mabel@mabelsfitstudio.example

t. 0781530462

w. www.mabelsfitstudio.example

```html
<!DOCTYPE html>
<html lang="en">
<head>
<meta charset="utf-8">
<title>Mabel's Fitness Business Cards</title>
<link href="https://fonts.googleapis.com/css2?family=Roboto:wght@300;400;500&display=swap" rel="stylesheet">
<style>
  :root {
    --backdrop: #e8e6e4;
    --card: #f4f3f1;
    --teal: #6db5bf;
    --taupe: #8f8482;
    --ink: #4a4a4a;
    --rule: #a9a3a1;
  }
  * { box-sizing: border-box; margin: 0; padding: 0; }
  html, body { width: 1200px; height: 997px; overflow: hidden; }
  body {
    background: var(--backdrop);
    font-family: "Roboto", Arial, sans-serif;
    color: var(--ink);
    position: relative;
  }
  .card {
    position: absolute;
    left: 320px;
    width: 560px;
    height: 320px;
    background: var(--card);
    box-shadow: 0 8px 22px rgba(0,0,0,0.12);
    overflow: hidden;
  }
  .card--front { top: 150px; }
  .card--back { top: 527px; }

  .brand {
    display: flex;
    align-items: center;
    gap: 14px;
  }
  .brand__mark {
    width: 46px; height: 46px;
    border-radius: 50%;
    border: 3px solid var(--teal);
    flex: none;
  }
  .brand__name {
    font-weight: 300;
    font-size: 24px;
    letter-spacing: 6px;
    text-transform: uppercase;
    color: var(--teal);
    white-space: nowrap;
  }

  .card--front .brand {
    position: absolute;
    top: 108px;
    left: 0; right: 0;
    justify-content: center;
  }
  .tagline {
    position: absolute;
    bottom: 62px;
    left: 0; right: 0;
    text-align: center;
    font-size: 15px;
    color: var(--ink);
  }

  .card--back .brand {
    position: absolute;
    top: 38px;
    right: 38px;
  }
  .card--back .brand__mark { width: 38px; height: 38px; }
  .card--back .brand__name { font-size: 19px; letter-spacing: 5px; }

  .website {
    position: absolute;
    top: 148px;
    right: 38px;
    font-size: 13px;
    color: var(--ink);
  }
  .divider {
    position: absolute;
    top: 172px;
    left: 38px; right: 38px;
    height: 1px;
    background: var(--rule);
  }
  .person {
    position: absolute;
    top: 186px;
    left: 38px;
  }
  .person__name {
    font-weight: 500;
    font-size: 19px;
    color: var(--teal);
    text-transform: uppercase;
  }
  .person__role {
    font-size: 14px;
    color: var(--taupe);
    text-transform: uppercase;
    margin-top: 2px;
  }
  .contact {
    list-style: none;
    margin-top: 12px;
    font-size: 13.5px;
  }
  .contact li {
    display: flex;
    align-items: center;
    gap: 8px;
    line-height: 20px;
  }
  .contact svg { width: 13px; height: 13px; fill: var(--teal); flex: none; }

  .band-rule {
    position: absolute;
    left: 0; right: 0;
    bottom: 14px;
    height: 2px;
    background: var(--rule);
  }
  .band {
    position: absolute;
    left: 0; right: 0;
    bottom: 0;
    height: 11px;
    background: var(--teal);
  }
</style>
</head>
<body>
  <section class="card card--front">
    <div class="brand">
      <span class="brand__mark"></span>
      <span class="brand__name">Mabel’s Fitness</span>
    </div>
    <p class="tagline">Become your happiest, healthiest &amp; strongest self</p>
  </section>

  <section class="card card--back">
    <div class="brand">
      <span class="brand__mark"></span>
      <span class="brand__name">Mabel’s Fitness</span>
    </div>
    <p class="website">www.mabelsfitstudio.example</p>
    <div class="divider"></div>
    <div class="person">
      <h1 class="person__name">Mabel Quint Harlow</h1>
      <p class="person__role">Personal Trainer</p>
      <ul class="contact">
        <li>
          <svg viewBox="0 0 24 24" aria-hidden="true"><path d="M6.6 10.8a15.1 15.1 0 0 0 6.6 6.6l2.2-2.2a1 1 0 0 1 1-.25 11.4 11.4 0 0 0 3.6.57 1 1 0 0 1 1 1V20a1 1 0 0 1-1 1A17 17 0 0 1 3 4a1 1 0 0 1 1-1h3.5a1 1 0 0 1 1 1c0 1.25.2 2.45.57 3.6a1 1 0 0 1-.25 1z"/></svg>
          0781530462
        </li>
        <li>
          <svg viewBox="0 0 24 24" aria-hidden="true"><path d="M2 5h20v14H2z M2 5l10 8 10-8" fill="var(--teal)"/><path d="M3 6l9 7 9-7" fill="none" stroke="#f4f3f1" stroke-width="1.6"/></svg>
          mabel@mabelsfitstudio.example
        </li>
      </ul>
    </div>
    <div class="band-rule"></div>
    <div class="band"></div>
  </section>
</body>
</html>
```